Stonefield General Contracting Business Card

My company is a General Contracting and Handyman service based in a private community in Northeast Pennsylvania.
Our cliental is a mix of year round and seasonal homeowners
We pride ourselves i using new and innovative building techniques and always try to build with pride and integrity
Please check my website f(under construction) or a list of services and more information
The files below are my logo and my facebook business page profile pic

Industry/Entity Type

Building

Contact Information for Business Card

Stonefield General Contracting
Dale Hurtig
Ashford Vale, Pennsylvania
570-314-2796
dale@stnfldco.com
www.stnfldco.com
www.pagenook.example/stonefieldcontracting

```html
<!DOCTYPE html>
<html lang="en">
<head>
<meta charset="utf-8">
<title>Stonefield General Contracting – Business Card</title>
<link rel="stylesheet" href="https://fonts.googleapis.com/css2?family=Archivo:wght@800&family=Arimo:wght@400&family=PT+Sans:wght@400;700&display=swap">
<style>
  :root {
    --backdrop: #4a2219;
    --card: #e6e6e7;
    --ink: #111111;
    --ink-soft: #1d1d1d;
    --accent: #c8202a;
    --photo-warm: #f5e7bf;
    --photo-cool: #eceef1;
  }
  * { box-sizing: border-box; margin: 0; padding: 0; }
  html, body { width: 1200px; height: 1000px; overflow: hidden; }
  body { background: var(--backdrop); position: relative; font-family: "PT Sans", sans-serif; }

  .card { position: absolute; left: 265px; width: 666px; height: 397px; background: var(--card); overflow: hidden; }
  .card--front { top: 73px; }
  .card--back { top: 532px; }

  .card__photo { position: absolute; inset: 0;
    background: linear-gradient(100deg, var(--photo-warm) 0%, #f3ecd8 38%, var(--photo-cool) 60%, #e7e9ec 100%); }

  .brand { position: absolute; display: flex; align-items: center; }
  .brand__mark { background: var(--accent); flex: none; }
  .brand__name { font-family: "Archivo", sans-serif; font-weight: 800; color: var(--ink); line-height: 1.05; }
  .brand__line { display: block; }

  .card--front .brand { left: 35px; top: 62px; gap: 64px; }
  .card--front .brand__mark { width: 55px; height: 55px; }
  .card--front .brand__line--main { font-size: 25px; }
  .card--front .brand__line--sub { font-size: 18px; }

  .person { position: absolute; left: 33px; top: 244px; font-size: 22px; font-weight: 700; color: var(--accent); }

  .contact { position: absolute; right: 33px; top: 174px; text-align: right; color: var(--ink-soft); font-size: 16px; }
  .contact__place { margin-bottom: 18px; }
  .contact__row { display: flex; justify-content: flex-end; align-items: center; gap: 7px; height: 21px; }
  .contact__row--gap { margin-top: 26px; }
  .contact__row--last { margin-top: 3px; }
  .icon { width: 15px; height: 15px; flex: none; }
  .icon--square { background: var(--accent); width: 14px; height: 14px; }

  .card--back .brand { left: 80px; top: 133px; gap: 57px; align-items: flex-start; }
  .card--back .brand__mark { width: 110px; height: 110px; }
  .card--back .brand__line--main { font-size: 36px; }
  .card--back .brand__line--sub { font-size: 24px; margin-top: 2px; }
  .back-contact { font-family: "Arimo", sans-serif; font-size: 14.5px; color: var(--ink-soft); margin-top: 6px; line-height: 21px; }
  .back-contact span + span { margin-left: 6px; }
</style>
</head>
<body>
  <section class="card card--front">
    <div class="card__photo" role="img" aria-label="Faded photo of a yellow hard hat, rolled blueprints, a folding ruler and a tape measure on building plans"></div>

    <div class="brand">
      <span class="brand__mark"></span>
      <span class="brand__name">
        <span class="brand__line brand__line--main">Stonefield</span>
        <span class="brand__line brand__line--sub">General Contracting</span>
      </span>
    </div>

    <p class="person">Dale Hurtig</p>

    <div class="contact">
      <p class="contact__place">Ashford Vale, Pennsylvania</p>
      <p class="contact__row">570-314-2796
        <svg class="icon" viewBox="0 0 16 16" aria-hidden="true"><path fill="#c8202a" d="M2 6c0-2 3-3 6-3s6 1 6 3l-2 1-1-1.6H5L4 7 2 6zm2 2h8l1 5H3l1-5zm4 1.2a1.8 1.8 0 1 0 0 3.6 1.8 1.8 0 0 0 0-3.6z"/></svg>
      </p>
      <p class="contact__row">dale@stnfldco.com
        <svg class="icon" viewBox="0 0 16 16" aria-hidden="true"><rect x="1" y="3" width="14" height="10" fill="#c8202a"/><path d="M1.5 3.5 8 9l6.5-5.5" fill="none" stroke="#fff" stroke-width="1.2"/></svg>
      </p>
      <p class="contact__row">www.stnfldco.com
        <svg class="icon" viewBox="0 0 16 16" aria-hidden="true"><circle cx="8" cy="8" r="7" fill="#c8202a"/><g fill="none" stroke="#fff" stroke-width="0.9"><ellipse cx="8" cy="8" rx="3" ry="7"/><path d="M1 8h14M2.2 4.5h11.6M2.2 11.5h11.6"/></g></svg>
      </p>
      <p class="contact__row contact__row--gap">stonefieldcontracting <span class="icon icon--square"></span></p>
      <p class="contact__row contact__row--last">Stonefield_Co <span class="icon icon--square"></span></p>
    </div>
  </section>

  <section class="card card--back">
    <div class="brand">
      <span class="brand__mark"></span>
      <div>
        <span class="brand__name">
          <span class="brand__line brand__line--main">Stonefield</span>
          <span class="brand__line brand__line--sub">General Contracting</span>
        </span>
        <p class="back-contact">Ashford Vale, Pennsylvania<br><span>570.314.2796</span><span>dale@stnfldco.com</span></p>
      </div>
    </div>
  </section>
</body>
</html>
```